Looking for business card/letterhead/email signature

Take existing logo and create full design suite of collateral

Contact Information for Business Card

Use mock details that can be edited by us

Font styles to use
Sans Serif

```html
<!DOCTYPE html>
<html lang="en">
<head>
<meta charset="utf-8">
<title>Harlow Digital – Business Cards</title>
<link rel="stylesheet" href="https://fonts.googleapis.com/css2?family=Fira+Sans:wght@400;600&display=swap">
<style>
  :root {
    --backdrop: #e2cbbb;
    --brand-blue: #0b3f89;
    --brand-blue-deep: #07337a;
    --paper: #f4f4f5;
    --ink: #3a3a3c;
    --accent-pink: #e0195f;
    --accent-cyan: #2aa3dc;
  }
  * { box-sizing: border-box; margin: 0; padding: 0; }
  html, body { width: 1200px; height: 1065px; overflow: hidden; }
  body {
    background: var(--backdrop);
    font-family: "Fira Sans", Arial, sans-serif;
    position: relative;
  }
  .card-sheet {
    position: absolute;
    left: 68px; top: 226px;
    width: 1084px; height: 620px;
    display: grid;
    grid-template-columns: 544px 540px;
    grid-template-rows: 310px 310px;
  }
  .card { position: relative; overflow: hidden; }
  .card--front {
    background: linear-gradient(180deg, var(--brand-blue) 0%, var(--brand-blue-deep) 100%);
    display: flex; align-items: center; justify-content: center;
  }
  .card--back { background: var(--paper); color: var(--ink); }

  .wordmark {
    display: flex; align-items: center; gap: 12px;
    font-weight: 600; letter-spacing: -0.5px;
  }
  .wordmark__dot { border-radius: 50%; background: var(--accent-pink); flex: none; }
  .card--front .wordmark { color: #ffffff; font-size: 52px; }
  .card--front .wordmark__dot { width: 22px; height: 22px; }
  .card--back .wordmark {
    position: absolute; right: 52px; top: 72px;
    color: var(--brand-blue); font-size: 30px; gap: 8px;
  }
  .card--back .wordmark__dot { width: 13px; height: 13px; }

  .holder { position: absolute; left: 52px; top: 78px; }
  .holder__name { color: var(--brand-blue); font-size: 19px; font-weight: 600; line-height: 1.2; }
  .holder__role { font-size: 13px; margin-top: 3px; }
  .divider {
    position: absolute; left: 52px; top: 154px;
    width: 60px; height: 1px; background: var(--brand-blue);
  }
  .address { position: absolute; left: 52px; top: 187px; font-size: 13px; line-height: 20px; }
  .contact { position: absolute; left: 52px; top: 237px; font-size: 13px; line-height: 20px; list-style: none; }
  .contact li { display: flex; align-items: center; gap: 6px; }
  .contact svg { width: 11px; height: 11px; flex: none; }
  .website {
    position: absolute; right: 60px; top: 257px;
    font-size: 13px; font-weight: 600; color: var(--brand-blue); line-height: 20px;
  }
</style>
</head>
<body>
<main class="card-sheet">
  <section class="card card--front">
    <div class="wordmark"><span class="wordmark__dot"></span>harlow digital</div>
  </section>

  <section class="card card--back">
    <div class="holder">
      <p class="holder__name">Dana Whitfield</p>
      <p class="holder__role">Managing Director</p>
    </div>
    <span class="divider"></span>
    <p class="address">Elmstead Court, Mill Lane<br>Ashcombe, Surrey KT9 4QP</p>
    <ul class="contact">
      <li><svg viewBox="0 0 12 12"><path d="M2.5 1 L4.5 1 L5.3 3.4 L4 4.4 Q5 7 7.6 8 L8.6 6.7 L11 7.5 L11 9.5 Q10.5 11 9 11 Q1 10 1 3 Q1 1.5 2.5 1 Z" fill="var(--accent-pink)"/></svg>000 000 0000</li>
      <li><svg viewBox="0 0 12 12"><rect x="0.6" y="2" width="10.8" height="8" fill="none" stroke="var(--accent-cyan)"/><path d="M0.6 2 L6 6.5 L11.4 2" fill="none" stroke="var(--accent-cyan)"/></svg>dana@harlowdigital.com</li>
    </ul>
    <p class="website">www.harlowdigital.com</p>
    <div class="wordmark"><span class="wordmark__dot"></span>harlow digital</div>
  </section>

  <section class="card card--back">
    <div class="holder">
      <p class="holder__name">Dana Whitfield</p>
      <p class="holder__role">Managing Director</p>
    </div>
    <span class="divider"></span>
    <p class="address">Elmstead Court, Mill Lane<br>Ashcombe, Surrey KT9 4QP</p>
    <ul class="contact">
      <li><svg viewBox="0 0 12 12"><path d="M2.5 1 L4.5 1 L5.3 3.4 L4 4.4 Q5 7 7.6 8 L8.6 6.7 L11 7.5 L11 9.5 Q10.5 11 9 11 Q1 10 1 3 Q1 1.5 2.5 1 Z" fill="var(--accent-pink)"/></svg>000 000 0000</li>
      <li><svg viewBox="0 0 12 12"><rect x="0.6" y="2" width="10.8" height="8" fill="none" stroke="var(--accent-cyan)"/><path d="M0.6 2 L6 6.5 L11.4 2" fill="none" stroke="var(--accent-cyan)"/></svg>dana@harlowdigital.com</li>
    </ul>
    <p class="website">www.harlowdigital.com</p>
    <div class="wordmark"><span class="wordmark__dot"></span>harlow digital</div>
  </section>

  <section class="card card--front">
    <div class="wordmark"><span class="wordmark__dot"></span>harlow digital</div>
  </section>
</main>
</body>
</html>
```